Nimbrel Computer Solutions
Business Technology Consulting
Professional
Gerald Pinto
1837 NE 41st Court
Lake Varden, FL 32780
gerald@nimbrelcs.com
www.nimbrelcs.com
My company file logo. Please contact me if another format is needed.

```html
<!DOCTYPE html>
<html lang="en">
<head>
<meta charset="utf-8">
<title>Nimbrel Computer Solutions – Business Cards</title>
<link rel="stylesheet" href="https://fonts.googleapis.com/css2?family=Arimo:wght@400;700&display=swap">
<style>
  :root {
    --page-bg: #e9e6e1;
    --card-bg: #ffffff;
    --card-shade: #e6e8ea;
    --brand-blue: #1d4f96;
    --ink: #2b2b2b;
    --ink-soft: #555555;
    --mark-faint: #eef0f2;
  }
  * { box-sizing: border-box; margin: 0; padding: 0; }
  html, body {
    width: 1200px; height: 902px; overflow: hidden;
    background: var(--page-bg);
    font-family: "Arimo", Arial, sans-serif;
  }
  .stage { position: relative; width: 1200px; height: 902px; }
  .card {
    position: absolute;
    width: 557px; height: 316px;
    border-radius: 20px;
    background: linear-gradient(160deg, var(--card-bg) 0%, var(--card-bg) 50%, var(--card-shade) 100%);
    box-shadow: 0 6px 18px rgba(0,0,0,0.22);
    overflow: hidden;
  }
  .card-front { left: 159px; top: 156px; z-index: 2; }
  .card-back { left: 447px; top: 442px; width: 562px; height: 318px; z-index: 1; }

  .brand { position: absolute; display: flex; flex-direction: column; align-items: center; transform: translateX(-50%); }
  .brand-dot { display: block; border-radius: 50%; background: var(--brand-blue); }

  .card-front .brand { left: 393px; top: 42px; }
  .card-front .brand-dot { width: 78px; height: 78px; margin-bottom: 20px; }
  .brand-name { color: var(--brand-blue); font-weight: 700; font-size: 21px; white-space: nowrap; line-height: 1.2; }

  .contact { position: absolute; left: 46px; top: 152px; color: var(--ink-soft); font-size: 11.5px; line-height: 14.8px; }
  .contact-name { color: var(--ink); font-size: 18px; font-weight: 700; line-height: 22px; margin-bottom: 24px; }
  .contact-web { margin-top: 16px; }

  .backdrop-disc {
    position: absolute; left: -12px; top: 8px;
    width: 300px; height: 300px; border-radius: 50%;
    background: var(--mark-faint);
  }
  .card-back .brand { left: 477px; top: 193px; }
  .card-back .brand-dot { width: 84px; height: 84px; margin-bottom: 12px; }
  .brand-web { color: var(--ink-soft); font-size: 11.5px; letter-spacing: 1px; white-space: nowrap; }
</style>
</head>
<body>
<main class="stage">
  <section class="card card-front">
    <div class="brand">
      <span class="brand-dot"></span>
      <span class="brand-name">Nimbrel Computer Solutions</span>
    </div>
    <div class="contact">
      <p class="contact-name">Gerald Pinto</p>
      <p>1837 NE 41st Court</p>
      <p>Lake Varden, FL 32780</p>
      <p>Phone: 239-555-0147</p>
      <p>Email: gerald@nimbrelcs.com</p>
      <p class="contact-web">www.nimbrelcs.com</p>
    </div>
  </section>

  <section class="card card-back">
    <span class="backdrop-disc"></span>
    <div class="brand">
      <span class="brand-dot"></span>
      <span class="brand-web">www.nimbrelcs.com</span>
    </div>
  </section>
</main>
</body>
</html>
```